UX Design Document Management App Project

UPDATED PROJECT and INCREASED TOTAL COST. Also added a new design guideline document (4KR - Concept - The Lattice 170613.pdf).

We are a small start-up company based in Sydney, Australia. We have the ideas and coding skills to have built a revolutionary document management app that helps knowledge workers deal with information overload.

We are about to launch an alpha version of a document management app on the iPhone. We have created a series of screens but they lack the brilliance that only a talented graphic designer can deliver. So we would like to find a design partner who can make a contribution in two areas:

1. Make specific changes to our screens such as formatting images so they better blend into the background.
2. Examine our overall UX and either suggest changes or propose new design concepts.
3. Create a logo for this product.

We have completed a pretty comprehensive design brief that we attach to this project and also a set of our existing screen designs in a mix of Photoshop and Keynote formats that we can share with you.

Once we have launched are alpha product, we hope that the winner of this project (our future graphic design partner) will work with us on another project that aims to radically improve the UX of our app in time for a full version 1.0 launch later this year.

We'd like to lock-down the alpha UX in 5 to 10 days but if the ideas you have are exciting enough we can extend this time.

Project now has a SIGNIFICANTLY INCREASED BUDGET (almost doubled) and an expanded scope to deliver a logo for our product. Check out the additional design brief document just uploaded.

Hello Designers,

Just to let you know that we have updated the project and INCREASED THE TOTAL BUDGET. We have also added a new design guideline document (4KR - Concept - The Lattice 170613.pdf) to help inspire you!

The project now has a significantly increased budget (almost doubled) and an expanded scope to also deliver a logo for our Quillmark product. Check out the additional design brief document just uploaded.

Thanks for participating!

All the best,

Dalton

Barring any unforeseen circumstances, this design competition will remain open until midnight Pacific Standard Time this Sunday. That means about 10 am Sydney time this Monday, July 1st. Good luck and get your designs in!

Project Deadline Extended
Reason: I agreed to use PST not AEST!

Target Market(s)

individual knowledge workers: professionals, office workers/managers, university students, academics/researchers, etc.

Industry/Entity Type

Graphic Designer

Requirements
Must have
• professional, highly effective UX

```html
<!DOCTYPE html>
<html lang="en">
<head>
<meta charset="utf-8">
<title>Document Summary App – Screens</title>
<link rel="stylesheet" href="https://fonts.googleapis.com/css2?family=Lato:wght@300;400&display=swap">
<style>
  :root {
    --page-bg: #0d1a2e;
    --lime: #8fd400;
    --ink-blue: #2f8fe0;
    --white: #ffffff;
    --card-text: #666a70;
    --card-muted: #9a9ea4;
    --chip-bg: #eceef0;
    --status-bg: #e9e9e9;
    --menu-bg: #1c1d1f;
    --menu-line: #3a3c3f;
    --menu-dim: #8a8c8f;
    --menu-bright: #f2f2f2;
  }
  * { box-sizing: border-box; margin: 0; padding: 0; }
  html, body { width: 1200px; height: 1040px; overflow: hidden; }
  body {
    background: var(--page-bg);
    font-family: "Lato", "Helvetica Neue", Arial, sans-serif;
    font-weight: 300;
    position: relative;
  }
  .screen {
    position: absolute;
    top: 165px;
    width: 400px;
    height: 710px;
    overflow: hidden;
    background: #2a2a2a;
  }
  .screen--overview { left: 150px; }
  .screen--menu { left: 650px; }

  .photo {
    position: absolute;
    inset: 0;
    background: radial-gradient(ellipse at 60% 35%, #9a9a9a 0%, #6e6e6e 35%, #3c3c3c 75%, #262626 100%);
  }

  .status-bar {
    position: absolute; top: 0; left: 0; right: 0; height: 22px;
    background: var(--status-bg);
    font-family: "Lato", Arial, sans-serif; font-weight: 400;
    font-size: 12px; color: #222;
    display: flex; align-items: center; justify-content: space-between;
    padding: 0 10px;
  }
  .status-bar .time { font-weight: 400; position: absolute; left: 50%; transform: translateX(-50%); }

  .hero-count {
    position: absolute; left: -19px; top: 101px;
    width: 172px; height: 172px; border-radius: 50%;
    background: var(--lime); color: var(--white);
    display: flex; flex-direction: column; align-items: center; justify-content: center;
    padding-left: 19px;
  }
  .hero-count .value { font-size: 66px; line-height: 1; font-weight: 300; }
  .hero-count .label { font-size: 24px; margin-top: 4px; }

  .stat {
    position: absolute; display: flex; align-items: center; gap: 6px;
    color: var(--white); font-size: 30px; line-height: 1;
  }
  .stat svg { width: 26px; height: 26px; fill: var(--white); }

  .summary-card {
    position: absolute; left: 23px; top: 380px; width: 355px; height: 282px;
    background: var(--white); border-radius: 6px; overflow: hidden;
  }
  .summary-card .title {
    color: var(--ink-blue); font-size: 25px; line-height: 1.15;
    padding: 16px 30px 0 30px; font-weight: 300;
  }
  .summary-meta {
    margin: 14px 30px 0 30px; height: 36px; background: var(--chip-bg);
    display: flex; justify-content: space-between; align-items: center;
    padding: 0 8px; font-size: 8px; color: #555; line-height: 1.3;
  }
  .summary-meta b { color: var(--ink-blue); font-weight: 400; }
  .summary-meta .read { text-align: right; }
  .summary-card .excerpt {
    padding: 12px 30px 0 30px; font-size: 10px; line-height: 1.45; color: var(--card-text);
  }
  .rating {
    position: absolute; left: 0; right: 0; bottom: 0; height: 62px;
    border-top: 1px solid #eee;
    display: flex; align-items: center; justify-content: center; gap: 10px;
    font-size: 13px; color: var(--card-muted);
  }
  .rating svg { width: 24px; height: 24px; }
  .star--on { fill: var(--lime); }
  .star--off { fill: none; stroke: #bbb; stroke-width: 1.5; }

  .chevron { position: absolute; left: 50%; transform: translateX(-50%); width: 34px; height: 10px; }
  .chevron path { fill: none; stroke: #cfcfcf; stroke-width: 4; stroke-linecap: round; }

  .menu-header { position: absolute; left: 0; right: 0; top: 0; height: 152px; overflow: hidden; }
  .menu-header .photo { background: radial-gradient(ellipse at 60% 40%, #8a8a8a 0%, #5a5a5a 45%, #2e2e2e 100%); }
  .menu-header .hero-dot {
    position: absolute; left: 0; top: 100px; width: 140px; height: 140px; border-radius: 50%;
    background: var(--lime); opacity: .85;
  }
  .menu-panel {
    position: absolute; left: 0; right: 0; top: 152px; bottom: 0;
    background: var(--menu-bg);
  }
  .menu-list { list-style: none; position: absolute; left: 0; right: 0; top: 78px; }
  .menu-item {
    height: 44px; display: flex; align-items: center; padding-left: 54px;
    font-size: 26px; color: var(--menu-bright);
    border-bottom: 1px solid var(--menu-line);
  }
  .menu-item + .menu-item { margin-top: 0; }
  .menu-item--dim { color: var(--menu-dim); }
  .menu-list .menu-item { height: 84px; padding-top: 0; }
  .menu-list .menu-item:first-child { height: 60px; }
  .menu-list .menu-item:last-child { border-bottom: none; }
</style>
</head>
<body>

<section class="screen screen--overview">
  <div class="photo" role="img" aria-label="Blurred black-and-white photograph of a steel truss bridge"></div>

  <div class="status-bar">
    <span>●●●○○ Operator</span>
    <span class="time">11:27 AM</span>
    <span>100 %</span>
  </div>

  <div class="hero-count"><span class="value">34</span><span class="label">Bridges</span></div>

  <div class="stat" style="left:26px;top:45px;">
    <svg viewBox="0 0 24 24"><circle cx="12" cy="12" r="11" fill="none" stroke="#fff" stroke-width="2"/><circle cx="12" cy="9" r="4"/><path d="M5 19c1.5-4 4-5 7-5s5.5 1 7 5z"/></svg>8
  </div>
  <div class="stat" style="left:130px;top:82px;">
    <svg viewBox="0 0 24 24"><rect x="4" y="8" width="6" height="14"/><rect x="12" y="3" width="8" height="19"/></svg>1
  </div>
  <div class="stat" style="left:168px;top:174px;">
    <svg viewBox="0 0 24 24"><path d="M12 2a7 7 0 0 0-7 7c0 5 7 13 7 13s7-8 7-13a7 7 0 0 0-7-7zm0 9.5A2.5 2.5 0 1 1 12 6.5a2.5 2.5 0 0 1 0 5z"/></svg>45
  </div>
  <div class="stat" style="left:130px;top:278px;">
    <svg viewBox="0 0 24 24"><path d="M2 22V10l6 4v-4l6 4v-4l6 4V3h2v19z"/></svg>3
  </div>
  <div class="stat" style="left:26px;top:312px;">
    <svg viewBox="0 0 24 24"><path d="M12 2a7 7 0 0 0-4 12.7V18h8v-3.3A7 7 0 0 0 12 2zm0 2a5 5 0 0 1 2.9 9.1l-.9.6V16h-4v-2.3l-.9-.6A5 5 0 0 1 12 4z"/><rect x="9" y="19" width="6" height="2"/></svg>2
  </div>

  <article class="summary-card">
    <h1 class="title">File name or Detected header</h1>
    <div class="summary-meta">
      <span><b>91</b> word summary<br>from <b>2,069</b> word original</span>
      <span class="read"><b>19</b> min. and<br>to read the original</span>
    </div>
    <p class="excerpt">In a est eu arcu mollis imperdiet. In laoreet nisi eget fermentum auctor. Vivamus porttitor egestas ullamcorper. Pellentesque tempus orci semper elit tempor tempor. Aliquam mollis massa id justo lacinia tristique.</p>
    <div class="rating">
      <span>Rate me:</span>
      <svg viewBox="0 0 24 24"><path class="star--on" d="M12 2l3 7h7l-5.5 4.5 2 7.5L12 17l-6.5 4 2-7.5L2 9h7z"/></svg>
      <svg viewBox="0 0 24 24"><path class="star--on" d="M12 2l3 7h7l-5.5 4.5 2 7.5L12 17l-6.5 4 2-7.5L2 9h7z"/></svg>
      <svg viewBox="0 0 24 24"><path class="star--on" d="M12 2l3 7h7l-5.5 4.5 2 7.5L12 17l-6.5 4 2-7.5L2 9h7z"/></svg>
      <svg viewBox="0 0 24 24"><path class="star--off" d="M12 2l3 7h7l-5.5 4.5 2 7.5L12 17l-6.5 4 2-7.5L2 9h7z"/></svg>
      <svg viewBox="0 0 24 24"><path class="star--off" d="M12 2l3 7h7l-5.5 4.5 2 7.5L12 17l-6.5 4 2-7.5L2 9h7z"/></svg>
    </div>
  </article>

  <svg class="chevron" style="top:680px;" viewBox="0 0 34 10"><path d="M3 3q14 6 28 0"/></svg>
</section>

<section class="screen screen--menu">
  <div class="menu-header">
    <div class="photo" role="img" aria-label="Blurred black-and-white photograph of a steel truss bridge"></div>
    <div class="hero-dot"></div>
  </div>
  <nav class="menu-panel">
    <svg class="chevron" style="top:30px;" viewBox="0 0 34 10"><path d="M3 3q14 6 28 0" style="stroke:#8a8c8f"/></svg>
    <ul class="menu-list">
      <li class="menu-item menu-item--dim">Bridgegraphic</li>
      <li class="menu-item menu-item--dim">Semantic Cloud</li>
      <li class="menu-item">Category Summary</li>
      <li class="menu-item">Text Summary</li>
      <li class="menu-item menu-item--dim">Full Text</li>
      <li class="menu-item">Word Cloud</li>
    </ul>
  </nav>
</section>

</body>
</html>
```